Independence Day Graphics for Sale

I want to create 10 social media graphics (new Pictora size 4:5 (1080 x 1350 pixels) focusing on our July 4th Sale Graphics, using any of the pics attached. Use the attached pics, NO RANDOM STOCK PHOTOGRAPHY. For the color scheme of the graphics, they should all be complementary to the product colors in the photos.
You can add any of the photos attached but none are required. You can do some of the graphics in all text. I mainly need BOLD text that says one of the headlines (10 total) SEE ATTACHED WORD DOCUMENT for the headlines to use.

Target Market(s)

women looking to lose weight

Requirements
Must have
• pics attached and text attached

```html
<!DOCTYPE html>
<html lang="en">
<head>
<meta charset="utf-8">
<title>July 4th Sale Graphics</title>
<link rel="stylesheet" href="https://fonts.googleapis.com/css2?family=Oswald:wght@700&display=swap">
<style>
  :root {
    --page-bg: #c8c8c8;
    --card-bg: #ffffff;
    --ink-top: #c27ca2;
    --ink-bottom: #6a2a52;
    --ink-soft-top: #d08cb0;
    --ink-soft-bottom: #8a3d68;
    --bracket: #dca3be;
    --dotted: #e23a4a;
  }
  * { margin: 0; padding: 0; box-sizing: border-box; }
  html, body { width: 1200px; height: 3460px; overflow: hidden; background: var(--page-bg); }
  .sheet { position: relative; width: 1200px; height: 3460px; }

  .card {
    position: absolute;
    width: 501px;
    height: 627px;
    background: var(--card-bg);
  }
  .card::before {
    content: "";
    position: absolute;
    top: 21px; left: 15px;
    width: 141px; height: 155px;
    border-top: 2px solid var(--bracket);
    border-left: 2px solid var(--bracket);
    border-top-left-radius: 8px;
  }
  .card::after {
    content: "";
    position: absolute;
    right: 9px; bottom: 15px;
    width: 134px; height: 134px;
    border-right: 2px solid var(--bracket);
    border-bottom: 2px solid var(--bracket);
    border-bottom-right-radius: 8px;
  }
  .col-left { left: 79px; }
  .col-right { left: 613px; }
  .row-1 { top: 81px; }
  .row-2 { top: 743px; }
  .row-3 { top: 1406px; }
  .row-4 { top: 2076px; }
  .row-5 { top: 2739px; }

  .offer-frame {
    position: absolute;
    border: 2px dotted var(--dotted);
  }

  .headline {
    position: absolute;
    left: -300px; right: -300px;
    text-align: center;
    white-space: nowrap;
    font-family: "Oswald", "Arial Narrow", sans-serif;
    font-weight: 700;
    line-height: 1.1;
    text-transform: uppercase;
    background: linear-gradient(to bottom, var(--ink-top) 20%, var(--ink-bottom) 85%);
    -webkit-background-clip: text;
    background-clip: text;
    color: transparent;
    transform: translateY(-55%) scaleX(var(--sx, 0.82));
  }
  .headline.soft {
    background: linear-gradient(to bottom, var(--ink-soft-top) 20%, var(--ink-soft-bottom) 85%);
    -webkit-background-clip: text;
    background-clip: text;
  }
  .headline.spaced { letter-spacing: 0.12em; padding-left: 0.12em; }
  .headline.wide { letter-spacing: 0.45em; padding-left: 0.45em; }
  .headline.airy { letter-spacing: 0.2em; padding-left: 0.2em; }
</style>
</head>
<body>
<main class="sheet">

  <section class="card col-left row-1">
    <div class="offer-frame" style="left:34px;top:310px;width:446px;height:150px;"></div>
    <p class="headline" style="top:114px;font-size:133px;">July 4th</p>
    <p class="headline" style="top:246px;font-size:100px;">Mega Sale!</p>
    <p class="headline" style="top:383px;font-size:133px;">25% Off</p>
    <p class="headline" style="top:534px;font-size:98px;">Everything</p>
  </section>

  <section class="card col-right row-1">
    <div class="offer-frame" style="left:50px;top:163px;width:400px;height:100px;"></div>
    <p class="headline" style="top:95px;font-size:113px;">Biggest</p>
    <p class="headline" style="top:212px;font-size:88px;">4th of July</p>
    <p class="headline" style="top:316px;font-size:98px;">Sale Ever!</p>
    <p class="headline" style="top:430px;font-size:110px;">25% Off</p>
    <p class="headline spaced" style="top:542px;font-size:95px;">Sitewide</p>
  </section>

  <section class="card col-left row-2">
    <div class="offer-frame" style="left:16px;top:356px;width:460px;height:140px;"></div>
    <p class="headline" style="top:94px;font-size:111px;">Historic</p>
    <p class="headline" style="top:202px;font-size:88px;">4th of July</p>
    <p class="headline wide" style="top:292px;font-size:100px;">Sale!</p>
    <p class="headline" style="top:427px;font-size:128px;">25% Off</p>
    <p class="headline" style="top:551px;font-size:78px;">Of Everything</p>
  </section>

  <section class="card col-right row-2">
    <div class="offer-frame" style="left:28px;top:310px;width:445px;height:150px;"></div>
    <p class="headline" style="top:112px;font-size:78px;">Mega Summer</p>
    <p class="headline" style="top:224px;font-size:115px;">Blowout!</p>
    <p class="headline" style="top:386px;font-size:126px;">25% Off</p>
    <p class="headline" style="top:536px;font-size:91px;">Everything</p>
  </section>

  <section class="card col-left row-3">
    <div class="offer-frame" style="left:27px;top:310px;width:446px;height:150px;"></div>
    <p class="headline" style="top:110px;font-size:126px;">One-Time</p>
    <p class="headline" style="top:230px;font-size:116px;">Only</p>
    <p class="headline" style="top:384px;font-size:120px;">25% Off</p>
    <p class="headline" style="top:542px;font-size:81px;">Of Everything!</p>
  </section>

  <section class="card col-right row-3">
    <div class="offer-frame" style="left:28px;top:46px;width:445px;height:317px;"></div>
    <p class="headline" style="top:152px;font-size:146px;--sx:0.72;">25% Off</p>
    <p class="headline" style="top:290px;font-size:86px;--sx:0.70;">Stock-Up Event</p>
    <p class="headline" style="top:435px;font-size:116px;">25% Off</p>
    <p class="headline" style="top:544px;font-size:72px;--sx:0.76;">All Supplements</p>
  </section>

  <section class="card col-left row-4">
    <div class="offer-frame" style="left:27px;top:51px;width:446px;height:273px;"></div>
    <p class="headline soft" style="top:121px;font-size:90px;">The Lowest</p>
    <p class="headline airy" style="top:243px;font-size:120px;">Prices</p>
    <p class="headline" style="top:383px;font-size:67px;--sx:0.76;">We've Ever Offered!</p>
    <p class="headline" style="top:504px;font-size:116px;">25% Off</p>
  </section>

  <section class="card col-right row-4">
    <div class="offer-frame" style="left:28px;top:65px;width:445px;height:264px;"></div>
    <p class="headline" style="top:142px;font-size:105px;--sx:0.70;">Our Biggest</p>
    <p class="headline" style="top:263px;font-size:88px;--sx:0.66;">Discount Ever!</p>
    <p class="headline" style="top:415px;font-size:130px;">25% Off</p>
    <p class="headline" style="top:538px;font-size:93px;--sx:0.78;">Everything!</p>
  </section>

  <section class="card col-left row-5">
    <div class="offer-frame" style="left:34px;top:200px;width:446px;height:207px;"></div>
    <p class="headline" style="top:129px;font-size:96px;--sx:0.80;">Don’t Wait!</p>
    <p class="headline" style="top:302px;font-size:166px;--sx:0.67;">25% Off</p>
    <p class="headline" style="top:485px;font-size:103px;--sx:0.80;">Ends Soon</p>
  </section>

  <section class="card col-right row-5">
    <div class="offer-frame" style="left:28px;top:50px;width:445px;height:329px;"></div>
    <p class="headline" style="top:138px;font-size:120px;--sx:0.63;">Last Chance</p>
    <p class="headline" style="top:281px;font-size:141px;--sx:0.72;">25% Off</p>
    <p class="headline soft" style="top:452px;font-size:80px;">Time Is</p>
    <p class="headline" style="top:542px;font-size:88px;--sx:0.76;">Running Out!</p>
  </section>

</main>
</body>
</html>
```